Bref créative
Business Card for Real Estate Company
Larkfield Residences
Professional
Marcy Dunwell
Realtor
248 E. Corwin Ave. Suite 716
Anchorage, Alaska 40817
larkfieldtx@mailvista.example
www.larkfieldtx.example
Its a card for a Norcott Praine Realtor. Make sure in small print somewhere on card its states "Each Office Independently Owned and Operated"

```html
<!DOCTYPE html>
<html lang="en">
<head>
<meta charset="utf-8">
<title>Larkfield Residences – Business Card</title>
<link rel="stylesheet" href="https://fonts.googleapis.com/css2?family=Open+Sans:wght@400;600;700&display=swap">
<style>
  :root {
    --backdrop: #d9d9d9;
    --card: #ffffff;
    --brand-red: #9b1b24;
    --brand-grey: #7b7b7b;
    --text-dark: #3d3d3d;
    --text-mid: #5a5a5a;
    --edge-grey: #c9c9c9;
  }
  * { box-sizing: border-box; margin: 0; padding: 0; }
  html, body {
    width: 1200px; height: 901px; overflow: hidden;
    background: var(--backdrop);
    font-family: "Open Sans", Arial, sans-serif;
  }
  .stage { position: relative; width: 1200px; height: 901px; }
  .card {
    position: absolute;
    width: 630px; height: 360px;
    background: var(--card);
    border-radius: 18px;
    overflow: hidden;
    box-shadow: 0 8px 24px rgba(0,0,0,0.18);
  }
  .card--back { left: 90px; top: 60px; }
  .card--front { left: 480px; top: 480px; }

  /* back */
  .back-brand {
    position: absolute; left: 0; right: 0; top: 120px;
    display: flex; align-items: center; justify-content: center; gap: 12px;
  }
  .brand-square { width: 20px; height: 20px; background: var(--brand-red); flex: none; }
  .brand-name {
    font-weight: 600; font-size: 30px; letter-spacing: 2px;
    color: var(--brand-grey); text-transform: uppercase; white-space: nowrap;
  }
  .back-note {
    position: absolute; left: 0; right: 0; top: 250px;
    text-align: center; font-size: 15px; color: var(--text-mid);
  }

  /* front */
  .front-brand {
    position: absolute; left: 34px; top: 156px; width: 300px;
    display: flex; align-items: center; gap: 9px;
  }
  .front-brand .brand-square { width: 16px; height: 16px; }
  .front-brand .brand-name { font-size: 19px; letter-spacing: 1px; }
  .contact {
    position: absolute; left: 368px; top: 48px; width: 245px;
    color: var(--text-dark);
  }
  .agent-name { font-weight: 700; font-size: 19px; color: var(--brand-red); }
  .agent-title { font-size: 13px; margin-top: 2px; }
  .address { font-size: 12.5px; line-height: 1.4; margin-top: 16px; }
  .lines { list-style: none; margin-top: 14px; font-size: 12.5px; line-height: 1.45; }
  .lines li { display: flex; align-items: center; gap: 7px; }
  .lines svg { width: 13px; height: 13px; fill: var(--brand-red); flex: none; }
  .lines .email { font-size: 11.5px; }
  .footer-band { position: absolute; left: 0; bottom: 0; width: 630px; height: 64px; }
  .website {
    position: absolute; right: 24px; bottom: 14px;
    color: #fff; font-size: 13px; letter-spacing: 2px;
  }
</style>
</head>
<body>
<main class="stage">

  <section class="card card--back" aria-label="Card back">
    <div class="back-brand">
      <span class="brand-square"></span>
      <span class="brand-name">Larkfield Residences</span>
    </div>
    <p class="back-note">Each Office Independently Owned and Operated</p>
  </section>

  <section class="card card--front" aria-label="Card front">
    <div class="front-brand">
      <span class="brand-square"></span>
      <span class="brand-name">Larkfield Residences</span>
    </div>

    <div class="contact">
      <h1 class="agent-name">Marcy Dunwell</h1>
      <p class="agent-title">Realtor</p>
      <p class="address">248 E. Corwin Ave. Suite 716<br>Anchorage, Alaska 40817</p>
      <ul class="lines">
        <li><svg viewBox="0 0 16 16"><path d="M2 5c0-2 2-3 3-3l2 3-1.5 1.5c.8 1.8 2.2 3.2 4 4L11 9l3 2c0 1-1 3-3 3C6 14 2 10 2 5z"/></svg>(555) 204-7130</li>
        <li><svg viewBox="0 0 16 16"><rect x="4" y="1" width="8" height="14" rx="1.5"/><rect x="5.5" y="3" width="5" height="8" fill="#fff"/></svg>(555) 318-4625</li>
        <li><svg viewBox="0 0 16 16"><rect x="4" y="1" width="8" height="5"/><rect x="1" y="6" width="14" height="6" rx="1"/><rect x="4" y="10" width="8" height="5" fill="#fff" stroke="#9b1b24"/></svg>(555) 204-7191</li>
        <li class="email"><svg viewBox="0 0 16 16"><rect x="1" y="3" width="14" height="10" rx="1"/><path d="M1.5 3.5 8 9l6.5-5.5" fill="none" stroke="#fff" stroke-width="1.3"/></svg>larkfieldtx@mailvista.example</li>
      </ul>
    </div>

    <svg class="footer-band" viewBox="0 0 630 64" aria-hidden="true">
      <path d="M0 40 L300 40 Q310 40 318 30 L330 16 L630 16 L630 64 L0 64 Z" fill="var(--edge-grey)"/>
      <path d="M0 52 L300 52 Q312 52 320 42 L336 24 L630 24 L630 64 L0 64 Z" fill="#e6e6e6"/>
      <path d="M322 64 L342 30 Q348 22 360 22 L630 22 L630 64 Z" fill="var(--brand-red)"/>
    </svg>
    <span class="website">www.larkfieldtx.example</span>
  </section>

</main>
</body>
</html>
```